Business Consulting Business Card

professional business card with basic information (1) First and Last name (2) email address, (3) phone number, (4) website.

```html
<!DOCTYPE html>
<html lang="en">
<head>
<meta charset="UTF-8">
<title>Tidewell Capital – Business Card</title>
<link rel="stylesheet" href="https://fonts.googleapis.com/css2?family=Poppins:wght@400;500;600&display=swap">
<style>
  :root {
    --backdrop: #1b1c20;
    --card-dark: #25292d;
    --teal: #4bb8c4;
    --teal-light: #5cc8c2;
    --teal-deep: #4ea6c4;
    --white: #ffffff;
    --muted: #e4e8ea;
  }
  * { box-sizing: border-box; margin: 0; padding: 0; }
  html, body {
    width: 1200px; height: 800px; overflow: hidden;
    background: var(--backdrop);
    font-family: "Poppins", sans-serif;
  }
  .canvas {
    width: 1200px; height: 800px;
    display: flex; align-items: center; justify-content: center; gap: 50px;
  }
  .card {
    position: relative; width: 525px; height: 300px; overflow: hidden;
    border-radius: 3px;
    box-shadow: 0 18px 40px rgba(0,0,0,.45);
  }

  /* Front */
  .card-front {
    background: linear-gradient(160deg, var(--teal-light) 0%, var(--teal-deep) 100%);
    display: flex; align-items: center; justify-content: center;
  }
  .brand { display: flex; align-items: center; gap: 12px; color: var(--white); }
  .brand-dot { width: 30px; height: 30px; border-radius: 50%; background: var(--white); }
  .brand-name { font-weight: 500; font-size: 27px; letter-spacing: 4px; text-transform: uppercase; }

  /* Back */
  .card-back { background: var(--card-dark); color: var(--white); }
  .card-back .brand { position: absolute; top: 40px; right: 34px; }
  .card-back .brand-dot { width: 22px; height: 22px; background: var(--teal); }
  .card-back .brand-name { font-size: 20px; letter-spacing: 3px; }

  .accent-half {
    position: absolute; left: -16px; top: 116px;
    width: 32px; height: 32px; border-radius: 50%; background: var(--teal);
  }
  .holder { position: absolute; left: 34px; top: 110px; }
  .holder-name { font-weight: 600; font-size: 19px; letter-spacing: 1.5px; text-transform: uppercase; }
  .holder-role { color: var(--teal); font-size: 14px; margin-top: -2px; }

  .divider {
    position: absolute; left: 34px; right: 34px; top: 188px;
    height: 1px; background: var(--teal);
  }
  .contacts { position: absolute; left: 34px; top: 202px; list-style: none; }
  .contacts li {
    display: flex; align-items: center; gap: 8px;
    font-size: 11.5px; line-height: 20px; color: var(--muted);
  }
  .contacts .hl { color: var(--teal); }
  .contacts svg { width: 14px; height: 14px; flex: none; }

  .address {
    position: absolute; right: 34px; top: 202px;
    text-align: right; font-size: 11.5px; line-height: 20px; color: var(--muted);
  }
  .base-band {
    position: absolute; left: 0; right: 0; bottom: 0; height: 6px; background: var(--teal);
  }
</style>
</head>
<body>
<main class="canvas">
  <section class="card card-front">
    <div class="brand">
      <span class="brand-dot"></span>
      <span class="brand-name">Tidewell Capital</span>
    </div>
  </section>

  <section class="card card-back">
    <div class="brand">
      <span class="brand-dot"></span>
      <span class="brand-name">Tidewell Capital</span>
    </div>

    <span class="accent-half"></span>
    <div class="holder">
      <p class="holder-name">Aron Vale</p>
      <p class="holder-role">Manager</p>
    </div>

    <div class="divider"></div>

    <ul class="contacts">
      <li>
        <svg viewBox="0 0 14 14"><circle cx="7" cy="7" r="7" fill="var(--teal)"/><rect x="4.5" y="3" width="5" height="8" rx="1" fill="none" stroke="#25292d" stroke-width="1.2"/></svg>
        +44 2071 846 302
      </li>
      <li>
        <svg viewBox="0 0 14 14"><circle cx="7" cy="7" r="7" fill="var(--teal)"/><rect x="3.5" y="4.5" width="7" height="5" fill="none" stroke="#25292d" stroke-width="1.1"/><path d="M3.5 4.5 7 7.5 10.5 4.5" fill="none" stroke="#25292d" stroke-width="1.1"/></svg>
        hello@tidewellmail.com
      </li>
      <li>
        <svg viewBox="0 0 14 14"><circle cx="7" cy="7" r="7" fill="var(--teal)"/><circle cx="7" cy="7" r="3.6" fill="none" stroke="#25292d" stroke-width="1"/><path d="M3.4 7h7.2M7 3.4c-1.6 2-1.6 5.2 0 7.2M7 3.4c1.6 2 1.6 5.2 0 7.2" fill="none" stroke="#25292d" stroke-width=".9"/></svg>
        <span>www.<span class="hl">tidewellweb</span>.com</span>
      </li>
    </ul>

    <address class="address" style="font-style:normal">
      PO BOX 482<br>
      Harbor Street<br>
      4th Lane, Oregon 97035
    </address>

    <div class="base-band"></div>
  </section>
</main>
</body>
</html>
```